Company notecard redesign

We'd like a redesign done of our company notecards. We use these cards to hand-write messages to clients/potential clients. This could be thank-you cards, congratulations cards, check-in cards, etc. Current cards are 5.5" x 8.5" and fold in half (you'll see the fold mark on the scanned image). We would like the new cards to not fold, and just be 5.5" x 4.25". We do like the little dog head you'll see on the inside notecard scan as the dog is our logo. I've also attached our "professional" logo with our new tagline. Address info you see on the outside notecard scan is correct.

Target Market(s)

Brindlequay and CRM clients

Industry/Entity Type

It Company

Colors
3377b5
ffffff
fff8ef

Requirements
Must have
• Our logo, some contact info
Nice to have
• Dog head from our current notecard scan

```html
<!DOCTYPE html>
<html lang="en">
<head>
<meta charset="utf-8">
<title>Harwick Notecards</title>
<link href="https://fonts.googleapis.com/css2?family=Montserrat:wght@500;800&display=swap" rel="stylesheet">
<style>
  :root {
    --brand-blue: #3377b5;
    --cream: #fff8ef;
    --white: #ffffff;
    --navy: #16395e;
    --sky: #7fb0d2;
    --stage: #262626;
  }
  * { box-sizing: border-box; margin: 0; padding: 0; }
  html, body {
    width: 1200px; height: 900px; overflow: hidden;
    background: var(--stage);
    font-family: "Montserrat", Arial, sans-serif;
  }
  .card-set {
    position: absolute; left: 50px; top: 249px;
    display: flex; gap: 60px;
  }
  .notecard {
    position: relative; width: 520px; height: 402px; overflow: hidden;
  }
  /* Front */
  .notecard--front { background: var(--brand-blue); }
  .front-frame {
    position: absolute; inset: 20px;
    border: 4px solid var(--white);
  }
  .front-band {
    position: absolute; top: 0; bottom: 0; left: 170px; width: 180px;
    background: var(--cream);
    display: flex; flex-direction: column; align-items: center;
  }
  .wordmark {
    display: flex; flex-direction: column; align-items: center;
    color: var(--navy);
  }
  .wordmark__name {
    display: flex; align-items: center; gap: 6px;
    font-weight: 800; font-size: 30px; letter-spacing: 1px; line-height: 1;
  }
  .wordmark__dot {
    width: 16px; height: 16px; border-radius: 50%; background: var(--sky);
  }
  .wordmark__tagline {
    margin-top: 4px; font-weight: 500; font-size: 7.5px; letter-spacing: 1.2px;
    text-transform: uppercase; white-space: nowrap;
  }
  .front-band .wordmark { margin-top: 168px; }
  .front-band .wordmark__name { font-size: 23px; letter-spacing: 0.5px; gap: 5px; }
  .front-band .wordmark__dot { width: 13px; height: 13px; }
  .front-band .wordmark__tagline { font-size: 6.5px; letter-spacing: 0.9px; }
  .front-url {
    margin-top: auto; margin-bottom: 26px;
    color: var(--brand-blue); font-size: 10px; font-weight: 500; letter-spacing: 0.6px;
  }
  /* Back */
  .notecard--back { background: var(--white); }
  .notecard--back .wordmark {
    position: absolute; top: 24px; left: 50%; transform: translateX(-50%);
  }
  .contact-line {
    position: absolute; left: 16px; bottom: 22px;
    display: flex; align-items: center; gap: 10px;
    color: var(--sky); font-size: 9px; font-weight: 500;
  }
  .contact-item { display: flex; align-items: center; gap: 4px; white-space: nowrap; }
  .contact-item svg { width: 8px; height: 8px; fill: var(--navy); }
  .mascot-area {
    position: absolute; right: 0; bottom: 0;
    width: 88px; height: 76px;
    border-top-left-radius: 44px; border-top-right-radius: 30px;
    background: var(--sky);
  }
</style>
</head>
<body>
  <main class="card-set">
    <section class="notecard notecard--front">
      <div class="front-frame"></div>
      <div class="front-band">
        <div class="wordmark">
          <div class="wordmark__name">HARWICK <span class="wordmark__dot"></span></div>
          <div class="wordmark__tagline">A Cloud Consulting Company</div>
        </div>
        <div class="front-url">WWW.HARWICKTECH.COM</div>
      </div>
    </section>

    <section class="notecard notecard--back">
      <div class="wordmark">
        <div class="wordmark__name">HARWICK <span class="wordmark__dot"></span></div>
        <div class="wordmark__tagline">A Cloud Consulting Company</div>
      </div>
      <div class="contact-line">
        <span class="contact-item">
          <svg viewBox="0 0 10 10" aria-hidden="true"><path d="M2 0.5 L3.8 2.6 L2.9 3.6 Q4 6 6.4 7.1 L7.4 6.2 L9.5 8 L8.3 9.5 Q3 9 0.5 1.7 Z"/></svg>
          555.014.2910
        </span>
        <span class="contact-item">
          <svg viewBox="0 0 10 10" aria-hidden="true"><circle cx="5" cy="5" r="4.5"/></svg>
          www.HarwickTech.com
        </span>
        <span class="contact-item">
          <svg viewBox="0 0 10 10" aria-hidden="true"><path d="M5 0.3 A3.4 3.4 0 0 1 8.4 3.7 Q8.4 6 5 9.7 Q1.6 6 1.6 3.7 A3.4 3.4 0 0 1 5 0.3 Z"/></svg>
          1180 w elm row fairview in 40112
        </span>
      </div>
      <div class="mascot-area" role="img" aria-label="Company mascot artwork area"></div>
    </section>
  </main>
</body>
</html>
```